Famous Australian Web Brand (Zentrivo.com.au) Needs a New Website & Logo

Zentrivo.com.au is one of the leading domain name registration businesses in Australia and is looking for an overhaul of its website and brand.

Zentrivo.com.au current products/services include domain name registration, web hosting, web site creation and SSL certificates.

In this design contest on Quorvane, we would like designers to create a new logo and new website design for Zentrivo.com.au.

Here is what contest entrants will need to create:
- 1 new logo
- 1 new home page design
- 1 internal page (pricing page)

The winning designer will receive the main prize of $750. In addition to this, the winning designer will have the opportunity to work with Zentrivo for the build of the full website and may get ongoing design work from Zentrivo.

thank you all for your designs, we are after a web 2.0 look and feel, please dont use serif fonts, lets use modern and sleek ones, i will upload some samples of one we like shortly

header is to be in black with some texturing, white fonts and the call to action buttons are in green.

for the 6 free services, please use round edges for the images with the text under it, as i will upload shortly and we would like custome images, not stockimage types please

im uploading a sample of a background image for the header, which is black with texturing and also and image for the footer/middle of the page which has the correct shading of the grey for the middle section

please see file 8 for the look we are trying to get with our site and for font ideas

Reason: we have decided to extend the contest for another 3 days as a couple of designers have requested a bit more time

Target Market(s)

People that might need to buy a domain name or start a website: small business owners; entrepreneurs; bloggers; everyone from mum-and-dad website owners to tech savvy entrepreneurs. Geographically we will be targeting Australia but this should not influence the design.

Industry/Entity Type

Build

Requirements
Must have
• The logo should:
- Have the text "Zentrivo"
- Be positioned in the top left hand corner of the website
- Be either a wordmark, pictorial or abstract logo. That is, text-only logos are acceptable but we are also interested in receiving logos with a mark to the left that could somehow represents the business that we’re in

The homepage should:
- Feel modern, slick, web2.0
- Have a horizontal menu with 4 menu items: About Us | Contact Us | My Cart | Login
- Include the logo at the top
- Include the content from this Word Document
- Include the rough layout and style from this JPG template layout

The interior page should:
- Have the same look and feel as the home page
- Include the rough layout and style from this JPG attachment
- Include the content from this second Word Document
Nice to have
• - Grey, white and black primary colors
- Buttons that are green or lime green with a web2.0 call to action
- Full-width design (i.e. across the screen like Quorvane)
Should not have
• - Do not include overt Australian references. While we are an Australian business we do not want Australian flags, kangaroos or Barnaby Wollop in our logo or on our website.
- Do not use the current red color scheme in the design. We want to move away from this.

```html
<!DOCTYPE html>
<html lang="en">
<head>
<meta charset="utf-8">
<title>Zentrivo.com.au – Domain Names</title>
<link rel="stylesheet" href="https://fonts.googleapis.com/css2?family=Arimo:wght@400;700&display=swap">
<style>
  :root {
    --black: #000;
    --header-dark: #1f1f1f;
    --header-mid: #333;
    --topbar: #232323;
    --white: #fff;
    --light-text: #d8d8d8;
    --muted: #9a9a9a;
    --page-grey: #f2f2f2;
    --card-grey: #8c8c8c;
    --green: #6cbf2f;
    --green-dark: #3f8f18;
    --lime-text: #7bd13a;
    --ink: #111;
    --body-ink: #1a1a1a;
  }
  * { box-sizing: border-box; margin: 0; padding: 0; }
  html, body { width: 1200px; height: 900px; overflow: hidden; }
  body {
    position: relative;
    font-family: "Arimo", Arial, sans-serif;
    background: var(--page-grey);
    color: var(--ink);
  }
  .abs { position: absolute; }

  /* top utility bar */
  .utility-bar { left: 0; top: 0; width: 1200px; height: 25px; background: var(--topbar); border-bottom: 1px solid #3a3a3a; }
  .utility-links { right: 114px; top: 5px; font-size: 13px; color: var(--light-text); }
  .utility-links span { color: var(--light-text); }

  /* header */
  .site-header {
    left: 0; top: 25px; width: 1200px; height: 200px;
    background:
      repeating-linear-gradient(45deg, rgba(255,255,255,.025) 0 2px, transparent 2px 4px),
      linear-gradient(180deg, var(--header-mid), var(--header-dark) 60%, #262626);
    border-bottom: 1px solid #555;
  }
  .brand { left: 132px; top: 62px; display: flex; align-items: center; gap: 18px; }
  .brand-square { width: 70px; height: 70px; background: #4fa9c9; }
  .brand-name { font-size: 30px; font-weight: 700; color: var(--white); letter-spacing: 1px; text-transform: uppercase; }

  .call-box {
    left: 764px; top: 36px; width: 325px; height: 37px; border-radius: 4px;
    background: linear-gradient(180deg, #fafafa, #d6d6d6);
    font-size: 17px; color: #222; text-align: center; line-height: 37px;
  }

  .main-nav { left: 580px; top: 97px; width: 510px; height: 38px; display: flex; background: var(--black); }
  .main-nav a { color: var(--white); text-decoration: none; font-size: 14px; display: flex; align-items: center; justify-content: center; border-left: 1px solid #444; }
  .main-nav a.active { background: var(--white); color: var(--ink); border-left: none; gap: 8px; }
  .main-nav a.active::after { content: ""; border: 4px solid transparent; border-top: 5px solid var(--ink); margin-top: 5px; }

  .dropdown { left: 580px; top: 135px; width: 104px; background: var(--black); z-index: 3; }
  .dropdown a { display: block; height: 24px; line-height: 24px; padding-left: 8px; font-size: 11px; color: var(--white); text-decoration: none; border-bottom: 1px solid #333; }
  .dropdown a:last-child { border-bottom: none; height: 32px; line-height: 24px; }

  .domain-search { left: 113px; top: 153px; width: 468px; height: 39px; background: var(--white); border: 2px solid #bbb; display: flex; align-items: center; }
  .domain-search .prefix { flex: 1; padding-left: 10px; font-size: 20px; color: #777; }
  .domain-search .tld { width: 57px; height: 100%; border-left: 1px solid #ccc; font-size: 15px; color: #777; padding: 10px 0 0 8px; }
  .domain-search .tld-arrow { width: 26px; height: 100%; background: #7a7a7a; display: flex; align-items: center; justify-content: center; }
  .search-button {
    left: 600px; top: 155px; width: 106px; height: 37px; border-radius: 3px;
    background: linear-gradient(180deg, #8bd44e, var(--green) 50%, var(--green-dark));
    color: var(--white); font-size: 19px; text-align: right; padding-right: 8px; line-height: 37px;
  }
  .search-links { left: 116px; top: 201px; font-size: 12px; color: var(--light-text); display: flex; gap: 15px; }

  /* video band */
  .video-band { left: 0; top: 226px; width: 1200px; height: 75px; background: linear-gradient(180deg, #fff 0%, #f4f4f4 40%, #cfcfcf 100%); }
  .video-card { top: 229px; width: 255px; height: 68px; background: var(--card-grey); display: flex; align-items: center; }
  .video-thumb { width: 91px; height: 56px; margin-left: 10px; border: 2px solid var(--white); background: linear-gradient(135deg, #c9b8a6, #e8dcd0); position: relative; }
  .video-thumb svg { position: absolute; right: 8px; top: 12px; }
  .video-card p { margin-left: 22px; color: var(--white); font-size: 16px; line-height: 24px; }

  /* promo banner */
  .promo-banner { left: 317px; top: 302px; width: 566px; height: 61px; background: var(--black); border-radius: 3px; color: var(--white); font-size: 19px; line-height: 24px; padding: 5px 0 0 68px; }
  .promo-banner em { font-style: normal; color: var(--lime-text); }

  /* services grid */
  .service { width: 290px; }
  .service-image { width: 281px; height: 107px; border-radius: 4px; border: 1px solid #ccc; }
  .img-social { background: linear-gradient(135deg, #3b4a5c, #7a5a8a 45%, #2f6f86); }
  .img-people { background: linear-gradient(90deg, #3a3330, #8a7a6e 35%, #2c2826 60%, #a8978a); }
  .img-hosting { background: linear-gradient(90deg, #fbfbfb 0 57%, #2b2b2b 57%); }
  .service h3 { font-size: 17px; font-weight: 400; text-align: center; margin-top: 4px; line-height: 18px; }
  .service p { font-size: 11.4px; line-height: 14.4px; text-align: justify; color: var(--body-ink); margin-top: 2px; }

  /* footer */
  .site-footer { left: 0; top: 783px; width: 1200px; height: 117px; background: linear-gradient(180deg, #111, #000 40%, #1c1c1c); }
  .footer-col { top: 789px; width: 90px; }
  .footer-col h4 { font-size: 12.5px; font-weight: 400; color: var(--white); text-transform: uppercase; margin-bottom: 4px; }
  .footer-col a { display: block; height: 24px; padding: 5px 0 0 12px; font-size: 12px; color: var(--muted); text-decoration: none; border-top: 1px dashed #555; position: relative; width: 84px; }
  .footer-col a:first-of-type { border-top: none; }
  .footer-col a::before { content: ""; position: absolute; left: 1px; top: 9px; border: 3px solid transparent; border-left: 4px solid #777; }
  .contact-panel { left: 803px; top: 790px; width: 288px; height: 87px; background: var(--black); text-align: center; }
  .contact-panel .kicker { font-size: 13px; letter-spacing: 2.5px; color: var(--muted); padding-top: 1px; }
  .contact-panel .headline { font-size: 26px; letter-spacing: 4.5px; color: #aaa; line-height: 28px; }
  .contact-panel .phone { font-size: 24px; color: var(--white); line-height: 28px; padding-bottom: 6px; border-bottom: 1px dashed #888; margin: 0 20px; }
  .copyright { left: 803px; top: 881px; width: 260px; text-align: center; font-size: 12px; color: #888; }
</style>
</head>
<body>

<div class="abs utility-bar"></div>
<nav class="abs utility-links">About Us <span>|</span> Contact Us <span>|</span> My Cart <span>|</span> Login</nav>

<header class="abs site-header"></header>
<div class="abs brand">
  <div class="brand-square"></div>
  <div class="brand-name">Zentrivo.com.au</div>
</div>
<div class="abs call-box">Have a question? Call 1300 41 72 95</div>

<nav class="abs main-nav">
  <a class="active" href="#" style="width:104px">Domains</a>
  <a href="#" style="width:106px">Creator</a>
  <a href="#" style="width:91px">Email</a>
  <a href="#" style="width:104px">Hosting</a>
  <a href="#" style="width:105px">Mark</a>
</nav>
<div class="abs dropdown">
  <a href="#">Register Domains</a>
  <a href="#">Transfer Domains</a>
  <a href="#">Renew Domains</a>
  <a href="#">Name Servers</a>
</div>

<form class="abs domain-search">
  <span class="prefix">www.</span>
  <span class="tld">.com</span>
  <span class="tld-arrow"><svg width="12" height="8" viewBox="0 0 12 8"><path d="M0 0h12L6 7z" fill="#fff"/></svg></span>
</form>
<div class="abs search-button">SEARCH</div>
<div class="abs search-links"><span>Renew a domain</span><span>Transfer a domain</span><span>View Price List</span></div>

<div class="abs video-band"></div>
<div class="abs video-card" style="left:113px">
  <div class="video-thumb" role="img" aria-label="Video thumbnail of a presenter"><svg width="30" height="30" viewBox="0 0 30 30"><circle cx="15" cy="15" r="14" fill="#f26b1d" stroke="#fff" stroke-width="1.5"/><path d="M11 8l11 7-11 7z" fill="#fff"/></svg></div>
  <p>Everyone needs<br>a domain name</p>
</div>
<div class="abs video-card" style="left:474px">
  <div class="video-thumb" role="img" aria-label="Video thumbnail of a presenter"><svg width="30" height="30" viewBox="0 0 30 30"><circle cx="15" cy="15" r="14" fill="#f26b1d" stroke="#fff" stroke-width="1.5"/><path d="M11 8l11 7-11 7z" fill="#fff"/></svg></div>
  <p>How you can use<br>a domain name</p>
</div>
<div class="abs video-card" style="left:834px">
  <div class="video-thumb" role="img" aria-label="Video thumbnail of a presenter"><svg width="30" height="30" viewBox="0 0 30 30"><circle cx="15" cy="15" r="14" fill="#f26b1d" stroke="#fff" stroke-width="1.5"/><path d="M11 8l11 7-11 7z" fill="#fff"/></svg></div>
  <p>Why choose<br>Zentrivo</p>
</div>

<div class="abs promo-banner">Everything your business needs to be successful<br>online is <em>FREE</em> with every domain name.</div>

<section class="abs service" style="left:115px;top:368px">
  <div class="service-image img-social" style="margin-left:5px" role="img" aria-label="Collage of social media icons behind bold lettering"></div>
  <h3>Free 15 Page Website</h3>
  <p>Create a professional, full-featured website in min-utes without any technical knowledge. Choose from 4,000+ stunning website designs and customize your site with near-limitless options. Upload your own artwork for a truly personalised look.</p>
</section>
<section class="abs service" style="left:452px;top:368px">
  <div class="service-image img-people" style="margin-left:4px" role="img" aria-label="Grid of fashion portrait photographs"></div>
  <h3>Free Professional Email</h3>
  <p>Create a professional, full-featured website in min-utes without any technical knowledge. Choose from 4,000+ stunning website designs and customize your site with near-limitless options. Upload your own artwork for a truly personalised look.</p>
</section>
<section class="abs service" style="left:797px;top:368px">
  <div class="service-image img-hosting" role="img" aria-label="Blogging platform logos beside a sync symbol on dark panel"></div>
  <h3>Free Website Hosting</h3>
  <p>We provide the fast and secure hosting for your web-site. We take care of all the maintenance so all you have to do is create content for your site. Best of all, you don't have to pay a cent for hosting for as long as your domain is registered with us.</p>
</section>

<section class="abs service" style="left:115px;top:576px">
  <div class="service-image img-social" style="margin-left:5px" role="img" aria-label="Collage of social media icons behind bold lettering"></div>
  <h3>Free Search Engine Optimisation</h3>
  <p>What good is the best looking website if no one visits it? We thought about that too! All our sites are opti-mised for search engines by default to ensure that your website is found by Searchly and other search engines like Findora and Lookwise.</p>
</section>
<section class="abs service" style="left:452px;top:576px">
  <div class="service-image img-people" style="margin-left:4px" role="img" aria-label="Grid of fashion portrait photographs"></div>
  <h3>Free Business Class Support</h3>
  <p>This is a point of pride for us and we are here to help. We're available to you 24 hours a day, everyday. Many of our competitors don't even provide a phone number for you to call! You deserve the best, and we won't settle for providing anything less.</p>
</section>
<section class="abs service" style="left:797px;top:576px">
  <div class="service-image img-hosting" role="img" aria-label="Blogging platform logos beside a sync symbol on dark panel"></div>
  <h3>Guaranteed renewal price.</h3>
  <p>You'll never pay more to renew your domain name than the rate you paid when you initially registered it, or what our registration rate was when you trans-ferred. (The only exceptions would be if you took advantage of a limited-time, special price)</p>
</section>

<footer class="abs site-footer"></footer>
<div class="abs footer-col" style="left:141px"><h4>Zentrivo</h4><a href="#">Overview</a><a href="#">Pricing</a><a href="#">Renew</a><a href="#">Transfer</a></div>
<div class="abs footer-col" style="left:315px"><h4>Zentrivo</h4><a href="#">Overview</a><a href="#">Pricing</a><a href="#">Renew</a><a href="#">Transfer</a></div>
<div class="abs footer-col" style="left:489px"><h4>Zentrivo</h4><a href="#">Overview</a><a href="#">Pricing</a><a href="#">Renew</a><a href="#">Transfer</a></div>
<div class="abs footer-col" style="left:666px"><h4>Zentrivo</h4><a href="#">Overview</a><a href="#">Pricing</a><a href="#">Renew</a><a href="#">Transfer</a></div>
<div class="abs contact-panel">
  <div class="kicker">HAVE A QUESTION FOR US?</div>
  <div class="headline">CONTACT US</div>
  <div class="phone">1300 41 72 95</div>
</div>
<div class="abs copyright">Copyright@2010zentrivohost.com</div>

</body>
</html>
```